Financial Planning Business needs a business card design

We need a business card design that is for a new financial planning business based in Australia. We provide financial planning advice such as retirement planning, wealth creation, asset protection.

Attached is the logo design. On the front side of the business card needs to incorporate the following:
- adviser name
- adviser title (ie Managing Director)
- address
- phone number
- email
- website address

Ideally it should also have the business name and logo

On the back of the card I would like this to be black in colour with the business name and logo

I have been advised the font is "Cinzel" (regular and bold)

Industry/Entity Type

Financial

Requirements
Must have
• Logo and business name

Format to have as follows:
Ben xxxxxxxx
Managing Director / Senior Financial Adviser
address
phone email
website

```html
<!DOCTYPE html>
<html lang="en">
<head>
<meta charset="utf-8">
<title>Meridian Wealth Planning – Business Card</title>
<link href="https://fonts.googleapis.com/css2?family=Cinzel:wght@400;700&family=Open+Sans:wght@400&display=swap" rel="stylesheet">
<style>
  :root {
    --page-bg: #ececec;
    --card-bg: #ffffff;
    --brand-blue: #129fd2;
    --brand-grey: #a3a3a3;
    --text-dark: #222222;
    --text-title: #555555;
    --deco-light: #e2e2e2;
    --deco-mid: #c9c9c9;
    --card-edge: #d0d0d0;
  }
  * { margin: 0; padding: 0; box-sizing: border-box; }
  html, body {
    width: 1170px; height: 1200px; overflow: hidden;
    background: var(--page-bg);
  }
  .canvas { position: relative; width: 1170px; height: 1200px; }

  .card {
    position: absolute; width: 927px; height: 532px;
    background: var(--card-bg);
    border: 1px solid var(--card-edge);
    overflow: hidden;
  }
  .card--front { left: 208px; top: 42px; }
  .card--back  { left: 39px;  top: 618px; }

  /* Front */
  .name-marker {
    position: absolute; left: 0; top: 53px; width: 19px; height: 107px;
    background: var(--brand-grey);
  }
  .adviser-name {
    position: absolute; left: 38px; top: 68px;
    font-family: "Cinzel", serif; font-weight: 400;
    font-size: 38px; letter-spacing: 1px;
    color: var(--brand-blue);
  }
  .adviser-title {
    position: absolute; left: 38px; top: 115px;
    font-family: "Cinzel", serif; font-weight: 400;
    font-size: 28px; letter-spacing: 1px;
    color: var(--text-title);
  }

  .brand {
    position: absolute; right: 28px; top: 56px;
    display: flex; align-items: center; gap: 16px;
    font-family: "Cinzel", serif; font-weight: 400;
    color: var(--brand-blue);
  }
  .brand__square {
    width: 58px; height: 58px; background: var(--brand-grey);
  }
  .brand__name { line-height: 1; text-align: right; }
  .brand__name .line-main { display: block; font-size: 58px; }
  .brand__name .line-sub  { display: block; font-size: 24px; margin-top: 4px; letter-spacing: 0.5px; }

  .contact-list {
    position: absolute; left: 38px; top: 277px;
    list-style: none;
    font-family: "Open Sans", sans-serif; font-size: 22px;
    color: var(--text-dark);
  }
  .contact-list li {
    display: flex; align-items: center; gap: 10px;
    height: 36px;
  }
  .contact-list svg { width: 20px; height: 20px; fill: var(--brand-blue); flex: none; }

  .address {
    position: absolute; left: 38px; top: 451px;
    font-family: "Open Sans", sans-serif; font-size: 20px;
    color: var(--text-dark);
  }
  .band-grey {
    position: absolute; left: 0; top: 507px; width: 620px; height: 26px;
    background: var(--brand-grey);
  }
  .band-blue {
    position: absolute; left: 632px; top: 496px; width: 295px; height: 37px;
    background: var(--brand-blue);
  }

  /* Back */
  .back-decoration {
    position: absolute; left: 0; top: 8px; width: 512px; height: 524px;
    background: linear-gradient(160deg, var(--deco-light) 0%, var(--deco-mid) 100%);
  }
  .back-brand {
    position: absolute; right: 32px; top: 268px; text-align: right;
    font-family: "Cinzel", serif; font-weight: 400;
    color: var(--brand-blue); line-height: 1;
  }
  .back-brand .line-main { display: block; font-size: 66px; }
  .back-brand .line-sub  { display: block; font-size: 28px; margin-top: 6px; letter-spacing: 0.5px; }
  .back-website {
    position: absolute; right: 32px; top: 404px;
    font-family: "Open Sans", sans-serif; font-size: 23px;
    color: var(--text-dark);
  }
</style>
</head>
<body>
<div class="canvas">

  <section class="card card--front">
    <div class="name-marker"></div>
    <h1 class="adviser-name">Your Name</h1>
    <p class="adviser-title">Title</p>

    <div class="brand">
      <span class="brand__square"></span>
      <span class="brand__name">
        <span class="line-main">Meridian</span>
        <span class="line-sub">Wealth Planning</span>
      </span>
    </div>

    <ul class="contact-list">
      <li>
        <svg viewBox="0 0 20 20" aria-hidden="true"><circle cx="10" cy="10" r="9" fill="none" stroke="currentColor" stroke-width="2" style="stroke:var(--brand-blue)"/><path d="M6.5 5.5l2 0 1 3-1.3 1a6 6 0 0 0 2.8 2.8l1-1.3 3 1 0 2c-5 .5-9-3.5-8.5-8.5z"/></svg>
        <span>012-345-6789</span>
      </li>
      <li>
        <svg viewBox="0 0 20 20" aria-hidden="true"><rect x="6" y="3" width="8" height="5"/><rect x="2" y="8" width="16" height="8" rx="2"/><rect x="5" y="15" width="10" height="3"/></svg>
        <span>012-345-6789</span>
      </li>
      <li>
        <svg viewBox="0 0 20 20" aria-hidden="true"><path d="M2 5h16v11H2z"/><path d="M2 5l8 6 8-6" fill="none" stroke="#fff" stroke-width="1.6"/></svg>
        <span>info@meridianwealthplanning.com</span>
      </li>
      <li>
        <svg viewBox="0 0 20 20" aria-hidden="true"><circle cx="10" cy="10" r="9"/><path d="M1 10h18M10 1v18M4 4.5c4 2 8 2 12 0M4 15.5c4-2 8-2 12 0" fill="none" stroke="#fff" stroke-width="1.2"/><ellipse cx="10" cy="10" rx="4" ry="9" fill="none" stroke="#fff" stroke-width="1.2"/></svg>
        <span>www.meridianwealthplanning.com</span>
      </li>
    </ul>

    <p class="address">Sreet Name, City Name, Zip Code-00000</p>

    <div class="band-grey"></div>
    <div class="band-blue"></div>
  </section>

  <section class="card card--back">
    <div class="back-decoration" role="img" aria-label="Large brand decoration area"></div>
    <div class="back-brand">
      <span class="line-main">Meridian</span>
      <span class="line-sub">Wealth Planning</span>
    </div>
    <p class="back-website">www.meridianwealthplanning.com</p>
  </section>

</div>
</body>
</html>
```